Create a business Card for a Women Owned Business Body Positive Company. The winner we hope to work with on other projects coming up for grand opening for flyers, postcards, email marketing, facebook page, stationary, labels, tshirt design....
We would like if possible in the background of the card a infinity symbol or crown if it fits into the design if not it's ok. But I am open to all suggestions we had alot problems with the our new logo being created this time sad to say :(

Our colors are Royal Purple, Grey, Black Thank you in advance for your talent, you hard work and your submissions!
Delia and Harriet :)

my Logo is lantern meadow boutique which is purple and has a heart and infinity sign in it and my colors are purple silver and black only of another card i had done nothing else. My logo is LANTERN MEADOW BOUTIQUE LOGO

Industry/Entity Type

Retail

Contact Information for Business Card

website: www.lantrnmeadowboutiques.example email: sales@lanternmeadowboutique.example
Delia Rookwell & Harriet Quinlan Owners

Font styles to use
Script

Colors
b768aa

Requirements
Must have
• COLORS ARE PURPLE BLACK AND GREY
Nice to have
• INFINITY SIGNING IN THE BACKGROUND

```html
<!DOCTYPE html>
<html lang="en">
<head>
<meta charset="utf-8">
<title>Lantern Meadow Boutique – Business Cards</title>
<link rel="stylesheet" href="https://fonts.googleapis.com/css2?family=Cinzel:wght@400;600;700&display=swap">
<style>
  :root {
    --stage: #1e1e1e;
    --royal-purple: #673e9c;
    --purple-deep: #5b3290;
    --purple-ink: #6a3d9e;
    --silver: #ececec;
    --silver-shade: #d9d9d9;
    --black: #111111;
    --white: #ffffff;
  }
  * { box-sizing: border-box; margin: 0; padding: 0; }
  html, body {
    width: 1200px;
    height: 1000px;
    overflow: hidden;
    background: var(--stage);
    font-family: "Cinzel", serif;
  }
  .stage { position: relative; width: 1200px; height: 1000px; }

  .card {
    position: absolute;
    width: 700px;
    height: 420px;
    overflow: hidden;
  }
  .card--front { left: 78px; top: 57px; background: var(--royal-purple); color: var(--white); }
  .card--back {
    left: 401px; top: 522px;
    background: linear-gradient(180deg, var(--white) 0%, var(--silver) 55%, var(--silver-shade) 100%);
  }

  .ornament-slot {
    position: absolute;
    border-radius: 6px;
  }
  .card--front .ornament-slot {
    left: 192px; top: 80px; width: 316px; height: 100px;
    background: linear-gradient(180deg, rgba(255,255,255,0.16), rgba(255,255,255,0.06));
  }
  .card--back .ornament-slot {
    left: 390px; top: 28px; width: 210px; height: 68px;
    background: linear-gradient(180deg, rgba(106,61,158,0.20), rgba(106,61,158,0.08));
  }

  .brand-name {
    position: absolute;
    text-align: center;
    font-weight: 400;
    line-height: 1;
  }
  .brand-name .line-main { display: block; }
  .brand-name .line-sub { display: block; letter-spacing: 0.42em; }

  .card--front .brand-name { left: 0; width: 700px; top: 198px; }
  .card--front .line-main { font-size: 50px; }
  .card--front .line-sub { font-size: 20px; margin-top: 16px; }

  .card--back .brand-name { left: 325px; width: 340px; top: 113px; color: var(--purple-ink); }
  .card--back .line-main { font-size: 34px; }
  .card--back .line-sub { font-size: 14px; margin-top: 10px; color: var(--purple-ink); }

  .tagline {
    position: absolute;
    text-align: center;
    font-weight: 700;
    font-variant: small-caps;
    text-transform: lowercase;
  }
  .card--front .tagline { left: 0; width: 700px; top: 334px; font-size: 18px; line-height: 21px; }
  .card--back .tagline { left: 325px; width: 340px; top: 182px; font-size: 13px; line-height: 15px; color: #222; }

  .swoosh { position: absolute; left: 0; top: 0; }

  .owners {
    position: absolute;
    left: 44px; top: 260px;
    color: var(--white);
  }
  .owners .owner-name { display: block; font-size: 19px; line-height: 23px; font-weight: 600; }
  .owners .owner-role { display: block; font-size: 13px; margin-top: 4px; letter-spacing: 0.04em; opacity: 0.9; }

  .contact {
    position: absolute;
    display: flex;
    align-items: center;
    gap: 7px;
    color: var(--white);
    font-size: 15px;
    font-weight: 600;
    font-variant: small-caps;
    text-transform: lowercase;
  }
  .contact svg { flex: none; }
  .contact--phone { left: 44px; top: 354px; font-size: 16px; }
  .contact--email { left: 326px; top: 326px; }
  .contact--web { left: 326px; top: 354px; }
</style>
</head>
<body>
<main class="stage">

  <section class="card card--front" aria-label="Business card front">
    <div class="ornament-slot" role="img" aria-label="Decorative scrollwork ornament above the boutique name"></div>
    <h1 class="brand-name">
      <span class="line-main">LANTERN MEADOW</span>
      <span class="line-sub">BOUTIQUE</span>
    </h1>
    <p class="tagline">Proudly providing unique clothing to all<br>women, young ladies &amp; princesses.</p>
  </section>

  <section class="card card--back" aria-label="Business card back">
    <svg class="swoosh" width="700" height="420" viewBox="0 0 700 420" aria-hidden="true">
      <path d="M0,108 C180,200 380,250 700,236 L700,420 L0,420 Z" fill="var(--black)"/>
      <path d="M0,112 C170,215 380,262 700,254 L700,420 L0,420 Z" fill="var(--royal-purple)"/>
      <path d="M0,112 C170,215 380,262 700,254 L700,420 L0,420 Z" fill="var(--purple-deep)" opacity="0.25"/>
    </svg>

    <div class="ornament-slot" role="img" aria-label="Decorative scrollwork ornament above the boutique name"></div>
    <h2 class="brand-name">
      <span class="line-main">LANTERN MEADOW</span>
      <span class="line-sub">BOUTIQUE</span>
    </h2>
    <p class="tagline">Proudly providing unique clothing to<br>all women, young ladies &amp; princesses</p>

    <div class="owners">
      <span class="owner-name">Delia Rookwell</span>
      <span class="owner-name">Harriet Quinlan</span>
      <span class="owner-role">OWNERS</span>
    </div>

    <p class="contact contact--phone">
      <svg width="14" height="14" viewBox="0 0 24 24" aria-hidden="true"><path fill="#fff" d="M6.6 10.8a15 15 0 0 0 6.6 6.6l2.2-2.2a1 1 0 0 1 1-.25 11.4 11.4 0 0 0 3.6.57 1 1 0 0 1 1 1V20a1 1 0 0 1-1 1A17 17 0 0 1 3 4a1 1 0 0 1 1-1h3.5a1 1 0 0 1 1 1c0 1.25.2 2.45.57 3.6a1 1 0 0 1-.25 1z"/></svg>
      555-014-7730
    </p>
    <p class="contact contact--email">
      <svg width="17" height="14" viewBox="0 0 24 20" aria-hidden="true"><rect x="1" y="3" width="22" height="16" rx="1.5" fill="#fff"/><path d="M2 4l10 8 10-8" fill="none" stroke="var(--royal-purple)" stroke-width="2"/></svg>
      sales@lanternmeadowboutique.example
    </p>
    <p class="contact contact--web">
      <svg width="14" height="14" viewBox="0 0 24 24" aria-hidden="true"><g fill="none" stroke="#fff" stroke-width="2"><circle cx="12" cy="12" r="10"/><ellipse cx="12" cy="12" rx="4.5" ry="10"/><path d="M2 12h20"/></g></svg>
      www.lantrnmeadowboutiques.example
    </p>
  </section>

</main>
</body>
</html>
```